RTV Photography Business Card Design

I would like a business card designed in the shape of a camera.
Would like to see various camera designs. Would like to see what the card looks like in different colors. Would like to see which logo looks better on the various camera designs so please show me some with the white logo and some with the black logo. If you need a different file formats please let me know.
Project Deadline Extended Reason: My grandfather passed away and dealing with funeral plans so need to extend deadline. Added Tuesday, March 1, 2016
Project Deadline Extended
Reason: I just got back from out of town. My grandfather's passing was the primary focus for me these past few weeks and the funeral is over so now I will concentrate on picking my business card design. I really appreciate each designer who has taken the time to submit a design. Your effort has not gone unnoticed. I look forward to seeing more amazing designs.
Industry/Entity Type
Business
Contact Information for Business Card
Wren
757-418-2096
https://www.facebook.com/rtvphotographyfreelance/
DoraWren@rtv-photography.example
Look and feel

```html
<!DOCTYPE html>
<html lang="en">
<head>
<meta charset="utf-8">
<title>RTV Photography Business Card</title>
<link rel="stylesheet" href="https://fonts.googleapis.com/css2?family=Roboto:wght@400;500;700&display=swap">
<style>
  :root {
    --page-bg: #e9e7e4;
    --card-bg: #222222;
    --gold: #c99a45;
    --gold-deep: #b9803a;
    --text-light: #e4e4e4;
  }
  html, body {
    margin: 0;
    padding: 0;
    width: 1200px;
    height: 1000px;
    overflow: hidden;
    background: var(--page-bg);
    font-family: "Roboto", Arial, sans-serif;
  }
  .business-card {
    position: absolute;
    left: 242px;
    top: 296px;
    width: 716px;
    height: 408px;
    border-radius: 22px;
    background: var(--card-bg);
    box-shadow: 0 6px 18px rgba(0,0,0,0.25);
  }
  .brand-mark {
    position: absolute;
    left: 482px;
    top: 18px;
    width: 94px;
    height: 94px;
    border-radius: 50%;
    background: var(--gold);
  }
  .brand-name {
    position: absolute;
    left: 330px;
    top: 140px;
    width: 340px;
    text-align: right;
    font-size: 27px;
    font-weight: 400;
    letter-spacing: 1px;
    color: var(--gold);
    white-space: nowrap;
  }
  .holder-name {
    position: absolute;
    left: 46px;
    top: 205px;
    margin: 0;
    font-size: 26px;
    font-weight: 700;
    letter-spacing: 0.5px;
    color: var(--gold-deep);
  }
  .contact-list {
    position: absolute;
    left: 46px;
    top: 262px;
    margin: 0;
    padding: 0;
    list-style: none;
  }
  .contact-item {
    display: flex;
    align-items: center;
    height: 31.5px;
    font-size: 16px;
    color: var(--text-light);
    letter-spacing: 0.2px;
  }
  .contact-icon {
    width: 12px;
    height: 14px;
    margin-right: 8px;
    flex: none;
  }
  .social-square {
    width: 9px;
    height: 9px;
    margin: 0 11px 0 2px;
    background: var(--gold);
    flex: none;
  }
</style>
</head>
<body>
  <div class="business-card">
    <div class="brand-mark" aria-hidden="true"></div>
    <div class="brand-name">RTV PHOTOGRAPHY</div>

    <h1 class="holder-name">WREN</h1>

    <ul class="contact-list">
      <li class="contact-item">
        <svg class="contact-icon" viewBox="0 0 12 14" aria-hidden="true">
          <rect x="2.5" y="0.5" width="7" height="13" rx="1.2" fill="none" stroke="#c99a45" stroke-width="1.2"/>
          <line x1="5" y1="11.3" x2="7" y2="11.3" stroke="#c99a45" stroke-width="1.2"/>
        </svg>
        757-418-2096
      </li>
      <li class="contact-item">
        <span class="social-square" aria-hidden="true"></span>
        rtvphotographyfreelance
      </li>
      <li class="contact-item">
        <svg class="contact-icon" viewBox="0 0 12 14" aria-hidden="true">
          <rect x="0" y="3" width="12" height="8.5" fill="#c99a45"/>
          <polyline points="0.4,3.4 6,8 11.6,3.4" fill="none" stroke="#222222" stroke-width="1"/>
        </svg>
        DoraWren@rtv-photography.example
      </li>
    </ul>
  </div>
</body>
</html>
```